Serlivo Business Cards

We need new Business Cards for our startup. It just launched.It is working in the high-end it-market. Specifically in the cloud area. We are a hybrid cloud company. The company logo is attached. We are a Swiss based company. Information visible on the card is: 1. Logo 2. Company Name: Serlivo AG 3. Subtitle: Hybrid Clouds. 3. Name: Tobias Ferrand 4. Adress: Lindenhofweg 14a, 8274 Tallenwil, Switzerland 5. Email: tobias@serlivo-mail.ch. 6. Mobile: +41 79 386 42 15. It should be a grey/white design. Similar to the attached logo. It should have class, high-quality but not too much color and no gold used.
Updates

I forgot to add my Position. Please use Founder / CEO. thanks tobias

Industry/Entity Type

Business

```html
<!DOCTYPE html>
<html lang="en">
<head>
<meta charset="utf-8">
<title>Serlivo Business Card</title>
<link rel="stylesheet" href="https://fonts.googleapis.com/css2?family=Open+Sans:wght@300;400&display=swap">
<style>
  :root {
    --backdrop: #2b2b2b;
    --card-white: #ffffff;
    --card-mist: #d9d9d9;
    --band-dark: #595959;
    --band-deep: #4d4d4d;
    --rule-light: #e6e6e6;
    --brand-grey: #4a4a4a;
    --text-light: #f2f2f2;
    --text-soft: #d6d6d6;
    --icon-fill: #ededed;
    --icon-ink: #555555;
  }
  * { margin: 0; padding: 0; box-sizing: border-box; }
  html, body {
    width: 1200px;
    height: 799px;
    overflow: hidden;
    background: var(--backdrop);
    font-family: "Open Sans", "Segoe UI", sans-serif;
  }
  .business-card {
    position: absolute;
    left: 150px;
    top: 142px;
    width: 900px;
    height: 514px;
    overflow: hidden;
    background: var(--band-dark);
    box-shadow: 0 18px 40px rgba(0,0,0,0.45);
  }
  .card-top {
    position: absolute;
    left: 0; top: 0;
    width: 100%;
    height: 206px;
    background: radial-gradient(ellipse at 45% 20%, var(--card-white) 0%, #f3f3f3 45%, var(--card-mist) 100%);
  }
  .brand {
    position: absolute;
    left: 300px;
    top: 74px;
    display: flex;
    align-items: center;
    gap: 26px;
  }
  .brand-dot {
    width: 58px;
    height: 58px;
    border-radius: 50%;
    background: var(--brand-grey);
  }
  .brand-name {
    font-weight: 300;
    font-size: 40px;
    letter-spacing: 14px;
    color: var(--brand-grey);
    text-transform: uppercase;
  }
  .band-edge {
    position: absolute;
    left: 0;
    top: 206px;
    width: 100%;
    height: 8px;
    background: var(--band-deep);
  }
  .band-rule {
    position: absolute;
    left: 0;
    top: 214px;
    width: 100%;
    height: 4px;
    background: var(--rule-light);
  }
  .card-bottom {
    position: absolute;
    left: 0; top: 218px;
    width: 100%;
    height: 296px;
    background: linear-gradient(180deg, #5f5f5f 0%, var(--band-dark) 60%, #525252 100%);
  }
  .person {
    position: absolute;
    right: 640px;
    top: 58px;
    text-align: right;
  }
  .person-name {
    font-weight: 300;
    font-size: 33px;
    color: var(--text-light);
    white-space: nowrap;
  }
  .person-role {
    margin-top: 8px;
    font-size: 15px;
    color: var(--text-soft);
  }
  .divider {
    position: absolute;
    left: 282px;
    top: 24px;
    width: 1px;
    height: 190px;
    background: rgba(255,255,255,0.45);
  }
  .contact-list {
    position: absolute;
    left: 300px;
    top: 44px;
    list-style: none;
  }
  .contact-item {
    display: flex;
    align-items: center;
    gap: 18px;
    height: 56px;
    font-size: 18px;
    color: var(--text-light);
    white-space: nowrap;
  }
  .contact-icon {
    width: 24px;
    height: 24px;
    flex: none;
  }
</style>
</head>
<body>
  <article class="business-card">
    <header class="card-top">
      <div class="brand">
        <span class="brand-dot"></span>
        <span class="brand-name">Serlivo</span>
      </div>
    </header>
    <div class="band-edge"></div>
    <div class="band-rule"></div>
    <section class="card-bottom">
      <div class="person">
        <div class="person-name">Tobias Ferrand</div>
        <div class="person-role">Founder / CEO</div>
      </div>
      <div class="divider"></div>
      <ul class="contact-list">
        <li class="contact-item">
          <svg class="contact-icon" viewBox="0 0 24 24" aria-hidden="true">
            <rect x="0" y="0" width="24" height="24" rx="4" fill="var(--icon-fill)"/>
            <path d="M8 5 L10.5 5 L11.5 9 L10 10.5 C10.8 12.5 11.8 13.6 13.5 14.3 L15 12.8 L19 13.8 L19 16.5 C19 17.5 18 18.5 16.8 18.3 C11 17.5 6.5 13 5.8 7.2 C5.6 6 6.6 5 8 5 Z" fill="var(--icon-ink)"/>
          </svg>
          <span>+41 79 386 42 15</span>
        </li>
        <li class="contact-item">
          <svg class="contact-icon" viewBox="0 0 24 24" aria-hidden="true">
            <rect x="0" y="0" width="24" height="24" rx="4" fill="var(--icon-fill)"/>
            <rect x="4.5" y="7" width="15" height="10.5" fill="none" stroke="var(--icon-ink)" stroke-width="1.6"/>
            <path d="M4.5 7 L12 13 L19.5 7" fill="none" stroke="var(--icon-ink)" stroke-width="1.6"/>
          </svg>
          <span>tobias@serlivo-mail.ch</span>
        </li>
        <li class="contact-item">
          <svg class="contact-icon" viewBox="0 0 24 24" aria-hidden="true">
            <rect x="0" y="0" width="24" height="24" rx="4" fill="var(--icon-fill)"/>
            <path d="M4.5 12 L12 5 L19.5 12" fill="none" stroke="var(--icon-ink)" stroke-width="1.8"/>
            <path d="M7 11 L7 19 L17 19 L17 11" fill="none" stroke="var(--icon-ink)" stroke-width="1.6"/>
            <rect x="10.5" y="14" width="3" height="5" fill="var(--icon-ink)"/>
          </svg>
          <span>Lindenhofweg 14a, 8274 Tallenwil, Switzerland</span>
        </li>
      </ul>
    </section>
  </article>
</body>
</html>
```